Bright Harbor Charity - helping the disadvantaged

I would like a new web site design for my charity BRIGHT HARBOR. The charity provides help for the disadvantaged. See current site
brightharbor.org.au for details. Please refer to the current site for information on the charity. The objectives of the charity are in the "about us" tab. You will also notice on the site that we provide information about events that we sponsor an area for this should be provided on the site.

Target Market(s)

We have two targets:
1. Individuals and Businesses that will donate money to the charity.
2. Individuals that are in need of support from the charity.

Industry/Entity Type

Charity

Requirements
Must have
• Ability for individuals to be able to understand the type of support we can provide.
Nice to have
• Our logo should be prominate on each pages
Should not have
• Should be use modern fonts

```html
<!DOCTYPE html>
<html lang="en">
<head>
<meta charset="utf-8">
<title>Bright Harbor – Announcements</title>
<link href="https://fonts.googleapis.com/css2?family=Cabin:wght@400;500&family=Dancing+Script:wght@500&display=swap" rel="stylesheet">
<style>
:root{
  --green:#4a9a2c;
  --green-dark:#3b7f22;
  --green-light:#6cb84a;
  --cream:#f6f5df;
  --cream-deep:#e9e8c8;
  --panel:#ffffff;
  --text:#555555;
  --muted:#777777;
  --rule:#a9c48f;
  --card-border:#c9c9c9;
}
*{margin:0;padding:0;box-sizing:border-box}
html,body{width:950px;height:1200px;overflow:hidden}
body{
  position:relative;
  font-family:"Cabin",sans-serif;
  color:var(--text);
  background:linear-gradient(#fbfbee 0,var(--cream) 250px,var(--cream-deep) 338px,var(--cream) 338px,var(--cream) 1083px,#efeed8 1083px,#f5f4e2 1200px);
}
.main-nav{
  position:absolute;left:85px;top:0;width:780px;height:30px;
  background:linear-gradient(#5fb23a,#3f8a22);
  border-radius:0 0 10px 10px;
  box-shadow:0 2px 3px rgba(0,0,0,.25);
  display:flex;justify-content:center;
}
.main-nav a{
  color:#fff;text-decoration:none;font-size:13px;line-height:28px;
  padding:0 15px;border-right:1px solid rgba(0,0,0,.18);
  box-shadow:1px 0 0 rgba(255,255,255,.15);
}
.main-nav a:last-child{border-right:none;box-shadow:none}
.brand{position:absolute;left:58px;top:64px}
.brand .welcome{font-family:"Dancing Script",cursive;color:var(--green);font-size:26px;display:block;margin-bottom:18px}
.brand .name{display:flex;align-items:center;gap:10px;margin-left:46px}
.brand .name span{font-size:34px;color:var(--green);letter-spacing:.5px}
.brand .name i{width:12px;height:12px;border-radius:50%;background:var(--green);display:block}
.featured{
  position:absolute;left:409px;top:45px;width:459px;height:282px;
  background:#efefef;border:2px solid #ccc;border-radius:8px;
  box-shadow:0 2px 4px rgba(0,0,0,.2);
}
.featured .poster{
  position:absolute;left:7px;top:7px;width:442px;height:229px;
  background:linear-gradient(#bfe6f7 0,#7cc9ee 60%,#9bd36a 82%,#4ea62c 100%);
}
.featured .caption{position:absolute;left:0;right:0;top:251px;text-align:center;color:var(--green);font-size:13px}
.content{
  position:absolute;left:60px;top:338px;width:830px;height:776px;
  background:var(--panel);box-shadow:0 0 4px rgba(0,0,0,.25);
}
.section-title{
  position:absolute;left:31px;top:33px;width:768px;height:32px;
  border-bottom:1px solid var(--rule);
  display:flex;justify-content:center;align-items:center;gap:8px;
  color:var(--green);font-size:20px;padding-bottom:6px;
}
.card{
  position:absolute;left:33px;width:765px;height:317px;
  border:1px solid var(--card-border);border-radius:6px;background:#fff;
  box-shadow:0 1px 3px rgba(0,0,0,.15);
}
.card h2{font-weight:400;font-size:16px;color:var(--green);position:absolute;left:12px;top:8px}
.card .banner{
  position:absolute;left:88px;top:42px;width:590px;height:162px;
  background:linear-gradient(#111 0,#111 55%,#2a2a2a 100%);
  box-shadow:0 12px 8px -6px rgba(0,0,0,.35);
}
.card p{position:absolute;left:13px;top:226px;width:730px;font-size:11.5px;line-height:16px;color:var(--text)}
.card .read-more{
  position:absolute;left:628px;top:280px;width:104px;height:23px;
  background:linear-gradient(var(--green-light),var(--green-dark));
  color:#fff;font-size:11.5px;text-align:center;line-height:23px;border-radius:3px;
  text-decoration:none;box-shadow:0 2px 2px rgba(0,0,0,.3);
}
.site-footer{position:absolute;left:60px;top:1124px;width:830px;font-size:11px;color:var(--muted)}
.site-footer nav a{color:var(--muted);text-decoration:none}
.site-footer nav span{margin:0 4px;color:#aaa}
.site-footer .copyright{position:absolute;right:0;top:0;text-align:right;line-height:16px;font-size:10px}
</style>
</head>
<body>
<nav class="main-nav">
  <a href="#">Home</a><a href="#">About Us</a><a href="#">Donate</a><a href="#">Apply</a><a href="#">Pledge</a><a href="#">Nominate</a><a href="#">Events</a><a href="#">Contact Us</a><a href="#">Directors</a><a href="#">Log In</a>
</nav>

<header class="brand">
  <span class="welcome">Welcome to</span>
  <div class="name"><i></i><span>BRIGHT HARBOR</span></div>
</header>

<aside class="featured">
  <div class="poster" role="img" aria-label="Event poster: Saturday 24th March Harmony Day at Oakrest Learning Centre, 10am till 3pm, with children holding hands on a grassy hill under a blue sky"></div>
  <div class="caption">HARMONY DAY</div>
</aside>

<main class="content">
  <h1 class="section-title">
    <svg width="20" height="16" viewBox="0 0 20 16" aria-hidden="true"><path d="M2 6h4l8-5v14l-8-5H2z" fill="#d9603a"/><path d="M4 10l2 5h2l-1-5" fill="#b04a2a"/><path d="M16 5q2 3 0 6" stroke="#d9603a" fill="none" stroke-width="1.5"/></svg>
    Announcements
  </h1>

  <article class="card" style="top:92px">
    <h2>Harmony Day Information Sheet &amp; Booking Form</h2>
    <div class="banner" role="img" aria-label="Harmony Day 24 March banner with a row of colourful paper people holding hands on black"></div>
    <p>Marlow Valley’s Inaugural Harmony Day Event 2012 Harmony Celebration Day – “EVERYONE BELONGS” Date: Saturday 24th March 2012 Venue: Oakrest Learning Centre, Linden Road, Marlow. Time: 10am – 3pm &nbsp; Harmony Day is celebrated around Australia on 21st March each year. It’s a day where all Australians celebrate our cultural diversity. The continuing message of Harmony...</p>
    <a class="read-more" href="#">Read more</a>
  </article>

  <article class="card" style="top:430px">
    <h2>Harmony Day</h2>
    <div class="banner" role="img" aria-label="Harmony Day 24 March banner with a row of colourful paper people holding hands on black"></div>
    <p>Harmony Day Saturday 24th March 2012 10am – 3pm &nbsp;Ivitation to have a stall…! Bright Harbor &amp; Oakrest will be holding a multicultural market and art exhibition combined with a community harmony day being held on site at…. Oakrest Learning Centre 15 – 17 Linden Road, Marlow &nbsp; Book your stall now and be a part of...</p>
    <a class="read-more" href="#">Read more</a>
  </article>
</main>

<footer class="site-footer">
  <nav><a href="#">Home</a><span>|</span><a href="#">About Us</a><span>|</span><a href="#">Donate</a><span>|</span><a href="#">Apply</a><span>|</span><a href="#">Pledge</a><span>|</span><a href="#">Nominate</a><span>|</span><a href="#">Events</a><span>|</span><a href="#">Contact Us</a><span>|</span><a href="#">Directors</a></nav>
  <div class="copyright">Copyright © 2012 Bright Harbor Proprietary Limited.<br>All Rights Reserved.</div>
</footer>
</body>
</html>
```